Bellwin, Horup & Bellwin Concussion Infographic

We need an infographic for a Bellwin, Horup & Bellwin, a personal injury law firm based in Florida. Our goal is to raise awareness about concussions targeted towards young teens. We have researched and gathered info on the symptoms, danger signs, what to do and not do after sustaining a concussion, and additional facts on the severity of concussions. Our main goal for this infographic is to create a well-designed, easy-to-read infographic that is visually appealing. The more graphics we can use to aid with the statistics we are offering, the better. What we don't want is just an infographic with a bunch of facts listed without any visual aids. We need a creative way to capture the audiences attention through eye-catching visuals so they will be enticed to read the statistics in the infographic.

Target Market(s)

high school sports teams, youth sports leagues,

Industry/Entity Type

Legal

Font styles to use
Serif

Colors
0355a3
33a6d7
ffffff
fece3e

Requirements
Must have
• Visual aids that compliment our stats, visually appealing imagery, cite our sources at the bottom of the infographic in fine print
Nice to have
• creative and visual ways to back up statistics, contains a flow both cognitively and visually - like a good story, conveying a message at a glance - taking alot of data and boiling it down to one image,
Should not have
• any pictures or visuals that may scare or turn off audience,

```html
<!DOCTYPE html>
<html lang="en">
<head>
<meta charset="UTF-8">
<title>Bellwin, Horup &amp; Bellwin Concussion Infographic</title>
<link href="https://fonts.googleapis.com/css2?family=Montserrat:wght@700;800&family=Work+Sans:wght@400;500;600;700&display=swap" rel="stylesheet">
<style>
  :root{
    --blue:#0355a3;
    --sky:#33a6d7;
    --white:#ffffff;
    --gold:#fece3e;
    --ink:#3a3a3a;
    --mist:#eef2f8;
    --panel:#e3eaf4;
    --cream:#fdf2d3;
    --cream-light:#fef8e8;
  }
  *{margin:0;padding:0;box-sizing:border-box;}
  html,body{width:837px;height:1200px;overflow:hidden;background:var(--white);}
  body{font-family:"Work Sans",Arial,sans-serif;color:var(--ink);}
  .infographic{position:relative;width:837px;height:1200px;overflow:hidden;}
  .abs{position:absolute;}

  .masthead{left:0;top:0;width:837px;height:122px;background:var(--blue);}
  .masthead-title{position:absolute;left:0;right:0;top:26px;text-align:center;color:var(--white);
    font-family:"Montserrat",Arial,sans-serif;font-weight:800;font-size:34px;line-height:40px;letter-spacing:1.2px;}

  .intro{left:0;top:122px;width:837px;height:140px;background:var(--mist);}
  .section-heading{font-family:"Work Sans",Arial,sans-serif;font-weight:700;color:var(--blue);font-size:17.6px;line-height:22px;}
  .body-text{font-size:12.6px;line-height:16.4px;}
  .accent{color:var(--blue);font-weight:600;}
  .accent-strong{color:var(--blue);font-weight:700;}
  .icon-ring{border-radius:50%;border:2px solid var(--blue);background:var(--white);}

  .stat-big{font-weight:700;color:var(--blue);}
  .divider{border-left:3px dotted var(--blue);}

  .symptoms-bg{left:0;top:430px;width:418px;height:224px;background:var(--cream);}
  .danger-bg{left:418px;top:430px;width:419px;height:224px;background:var(--cream-light);}
  .label{font-size:12.4px;line-height:16.4px;}

  .dont-panel{left:558px;top:654px;width:279px;height:386px;background:var(--panel);}
  .para{font-size:12.2px;line-height:16.4px;text-align:justify;}
  .para b{font-weight:600;color:#222;}
  .dont-item{font-size:12.4px;line-height:19.4px;}
  .dont-item b{font-weight:600;color:#222;}

  .footer{left:0;top:1040px;width:837px;height:160px;background:var(--blue);color:var(--white);}
  .footer .section-heading{color:var(--white);}
  .footer-text{font-size:12.6px;line-height:16.4px;}
</style>
</head>
<body>
<main class="infographic">

  <header class="abs masthead">
    <h1 class="masthead-title">BELLWIN, HORUP &amp; BELLWIN<br>CONCUSSION INFOGRAPHIC</h1>
  </header>

  <!-- What is a concussion -->
  <section class="abs intro" aria-label="What is a Concussion">
    <h2 class="abs section-heading" style="left:50px;top:20px;">What is a Concussion?</h2>
    <p class="abs body-text" style="left:50px;top:50px;width:272px;">A type of <span class="accent">traumatic brain injury</span> caused by a bump, jolt, or blow to the head or body which causes the brain to jerk back and forth rapidly inside the skull.</p>
    <div class="abs icon-ring" role="img" aria-label="Head with bandaged brain icon" style="left:347px;top:47px;width:74px;height:74px;background:radial-gradient(circle at 50% 45%,#f4c6c6 0 22%,#fff 23%);"></div>
    <p class="abs body-text" style="left:473px;top:50px;width:228px;">More than <span class="accent-strong">90%</span> of sport-related concussions occur <span class="accent-strong">WITHOUT</span> the person losing consciousness or being "knocked out."</p>
    <svg class="abs" style="left:706px;top:42px;" width="84" height="84" viewBox="0 0 84 84">
      <circle cx="42" cy="42" r="40" fill="none" stroke="var(--sky)" stroke-width="3" stroke-dasharray="200 52"/>
      <circle cx="42" cy="42" r="34" fill="var(--white)" stroke="var(--blue)" stroke-width="1.5"/>
    </svg>
    <div class="abs" role="img" aria-label="Head profile icon" style="left:728px;top:64px;width:40px;height:40px;border-radius:50%;background:#dfe7f2;"></div>
  </section>

  <!-- Frequency -->
  <section aria-label="How often concussions occur">
    <h2 class="abs section-heading" style="left:50px;top:275px;">How Often are People Sustaining Concussions From Sports?</h2>
    <div class="abs" role="img" aria-label="Running person icon" style="left:52px;top:318px;width:38px;height:50px;background:var(--blue);border-radius:19px 19px 6px 6px;opacity:.9;"></div>
    <div class="abs stat-big" style="left:94px;top:313px;font-size:29px;line-height:32px;">1.6 to 3.8<br>MILLION</div>
    <p class="abs" style="left:50px;top:378px;width:180px;font-size:11px;line-height:16px;">people are involved in a <b>sport-related</b> concussion each year.</p>
    <div class="abs divider" style="left:238px;top:316px;height:92px;"></div>

    <div class="abs" role="img" aria-label="Sprinting athlete icon" style="left:254px;top:322px;width:70px;height:76px;background:var(--blue);border-radius:35px 10px 30px 10px;opacity:.9;"></div>
    <p class="abs" style="left:336px;top:314px;font-size:14.5px;line-height:18px;">High school athletes</p>
    <p class="abs" style="left:336px;top:333px;font-size:11.4px;line-height:14px;">sustained an estimated of</p>
    <div class="abs stat-big" style="left:336px;top:344px;font-size:40px;line-height:48px;">300,000</div>
    <p class="abs" style="left:318px;top:390px;font-size:15.6px;line-height:19px;">concussions per year.</p>
    <div class="abs divider" style="left:524px;top:316px;height:92px;"></div>

    <p class="abs" style="left:530px;top:314px;width:172px;font-size:11px;line-height:17px;text-align:justify;"><span class="accent-strong" style="font-size:13px;">An Athlete</span> who has suffered from a concussion in the past, is <span class="accent-strong" style="font-size:16px;">3-6 times</span> more likely to suffer from another concussion compared to an athlete who has never had one.</p>
    <div class="abs" role="img" aria-label="Person silhouette outline icon" style="left:712px;top:322px;width:76px;height:82px;border:3px solid var(--blue);border-radius:38px 38px 14px 14px;"></div>
  </section>

  <!-- Symptoms & danger signs -->
  <div class="abs symptoms-bg"></div>
  <div class="abs danger-bg"></div>
  <svg class="abs" style="left:0;top:430px;" width="837" height="224" viewBox="0 0 837 224" aria-hidden="true">
    <g fill="none" stroke="#777" stroke-width="0.9">
      <path d="M118 60 H122 V95 H118"/><path d="M122 77 H165 L162 82"/>
      <path d="M256 60 H252 V95 H256"/><path d="M252 77 H222 L215 88"/>
      <path d="M256 122 H252 V146 H256"/><path d="M252 130 H226"/>
      <path d="M256 152 H252 V200 H256"/><path d="M252 186 H230 L196 152"/>
      <path d="M132 140 H136 V217 H132"/><path d="M136 178 H150 V136 L158 128"/>
    </g>
    <defs>
      <linearGradient id="ring" x1="0" y1="0" x2="1" y2="1">
        <stop offset="0" stop-color="var(--sky)"/><stop offset=".55" stop-color="var(--blue)"/><stop offset="1" stop-color="var(--gold)"/>
      </linearGradient>
    </defs>
    <circle cx="190" cy="118" r="36" fill="var(--white)" stroke="url(#ring)" stroke-width="3.5"/>
    <g fill="#555"><circle cx="165" cy="82" r="2.5"/><circle cx="215" cy="88" r="2.5"/><circle cx="226" cy="130" r="2.5"/><circle cx="196" cy="152" r="2.5"/><circle cx="158" cy="128" r="2.5"/></g>

    <path d="M418 68 A68 68 0 0 1 418 202" fill="none" stroke="var(--blue)" stroke-width="8"/>
    <path d="M418 60 A76 76 0 0 1 418 210" fill="none" stroke="var(--blue)" stroke-width="0" />
    <path d="M445 118 L464 152 H426 Z" fill="var(--blue)" stroke="var(--blue)" stroke-width="4" stroke-linejoin="round"/>
    <rect x="443" y="127" width="4" height="14" rx="1.5" fill="var(--white)"/>
    <circle cx="445" cy="146" r="2.3" fill="var(--white)"/>
    <g fill="none" stroke="var(--blue)" stroke-width="0.9">
      <path d="M470 90 L488 68 H507"/><path d="M509 62 H507 V96 H509"/>
      <path d="M482 128 L493 110 H507"/><path d="M509 104 H507 V138 H509"/>
      <path d="M485 150 H507"/><path d="M509 146 H507 V180 H509"/>
      <path d="M470 180 L488 197 H507"/><path d="M509 189 H507 V222 H509"/>
    </g>
  </svg>
  <div class="abs" role="img" aria-label="Swimmer, cyclist and runner icons" style="left:166px;top:524px;width:48px;height:48px;border-radius:50%;background:#d6e6f5;"></div>

  <h2 class="abs section-heading" style="left:43px;top:453px;">Symptoms Reported by Athlete</h2>
  <p class="abs label" style="left:43px;top:492px;">Nauseau or<br>vomiting</p>
  <p class="abs label" style="left:258px;top:492px;">Headache or<br>"pressure" in head</p>
  <p class="abs label" style="left:258px;top:544px;">Problems with<br>balance or dizziness</p>
  <p class="abs label" style="left:43px;top:575px;">Feeling hazy,<br>sluggish,<br>foggy, or<br>groggy</p>
  <p class="abs label" style="left:258px;top:592px;">Confusion, trouble<br>with concentration or<br>memory problems</p>

  <h2 class="abs section-heading" style="left:442px;top:453px;">Danger Signs</h2>
  <p class="abs label" style="left:511px;top:486px;width:300px;">One pupil (the black circular part in the middle of the eye) larger than the other</p>
  <p class="abs label" style="left:511px;top:528px;width:300px;">A headache that gets worse and does not go away</p>
  <p class="abs label" style="left:511px;top:570px;width:300px;">Loss of consciousness of more than a minute</p>
  <p class="abs label" style="left:511px;top:613px;width:300px;">Drowsiness or cannot be awakened</p>

  <!-- What to do -->
  <section aria-label="What to do after a concussion">
    <h2 class="abs section-heading" style="left:39px;top:675px;">What to Do After Sustaining a Concussion</h2>
    <p class="abs para" style="left:39px;top:712px;width:510px;"><b>Remove Athlete from Play.</b> Pay attention to any signs or symptoms of a concussion and keep athlete out of game when in doubt.</p>
    <p class="abs para" style="left:39px;top:758px;width:510px;"><b>Seek Medical Attention.</b> Ensure that the athlete is evaluated by a health care professional. Record the following information that may assist the health care professional:<br>
      <span style="display:block;text-align:left;">- cause of the injury and impact of the hit or blow to the head or body.<br>- any loss of consciousness, and if so, for how long.<br>- any memory loss right after the injury.<br>- number of previous concussions if any.</span></p>
    <p class="abs para" style="left:39px;top:887px;width:510px;"><b>Rest.</b> After a concussion the brain needs time to heal. This means avoiding activities that are physically demanding or require alot of concentration, which can slow your recovery or worsen your symptoms.</p>
    <p class="abs para" style="left:39px;top:950px;width:510px;"><b>Inform and Educate Parents.</b> It is important for the parents to speak with their health care professional as well as their kids to learn about all the symptoms of concussions, the proper steps to take in treating the injury, the potential long-term effects of concussions and the dangers of returing too soon to physically and mentally demanding activities.</p>
  </section>

  <!-- What not to do -->
  <aside class="abs dont-panel" aria-label="What not to do after a concussion">
    <h2 class="abs section-heading" style="left:21px;top:21px;line-height:23px;">What Not to Do<br>After a Concussion</h2>
    <p class="abs dont-item" style="left:21px;top:84px;width:205px;"><b>Physical Activity.</b> An activity that causes an increase in heart rate may worsen symptoms.</p>
    <p class="abs dont-item" style="left:21px;top:174px;width:205px;"><b>Strenuous Mental Activities.</b> Such as computer work, reading, playing video games and watching TV.</p>
    <p class="abs dont-item" style="left:21px;top:264px;width:205px;"><b>Driving.</b> Do not drive for at least 24 hours the injury. Reaction time may be slowed down which can increase the risk of accidents.</p>
  </aside>

  <!-- Additional information -->
  <footer class="abs footer">
    <h2 class="abs section-heading" style="left:39px;top:18px;">Additional Information</h2>
    <p class="abs footer-text" style="left:41px;top:64px;width:720px;">Teens generally require a longer recovery time than adults for concussions because their brains are still developing.</p>
    <p class="abs footer-text" style="left:41px;top:104px;width:720px;">Research indicates that <b>80-90%</b> of concussions will resolve within <b>7-10 days</b>, however depending on the person and severity of the concussion, may take much longer</p>
  </footer>

</main>
</body>
</html>
```